Portfolio site - Need a basic WordPress or SquareSpace site

I need a portfolio site where I have the option to keep updating it on my own. Therefore, I'm guessing I need one that uses WordPress or SquareSpace. I just need a simple and elegant design. I'm a writer (scholarly, fiction and journalism).

Target Market(s)

Adult

Industry/Entity Type

Writer

Number of Pages Required

4 page

Font styles to use
Serif

Colors
b7a5cd
e667a6
85abd2

Requirements
Must have
• Easily updatable features. I'll have to publish links and small blurbs from time to time. And maybe the occasional image.
• Pages should be:
• Home
• Work
• Press
• Contact

```html
<!DOCTYPE html>
<html lang="en">
<head>
<meta charset="utf-8">
<title>Selina Marlowe — Writer</title>
<link href="https://fonts.googleapis.com/css2?family=Playfair+Display:wght@400;700;900&family=Open+Sans:wght@400;600;700&display=swap" rel="stylesheet">
<style>
:root{
  --pink:#e0559e;
  --pink-soft:#e667a6;
  --lilac:#b7a5cd;
  --blue:#85abd2;
  --ink:#2a2a2a;
  --muted:#777;
  --grey:#f1f0f1;
  --white:#fff;
  --serif:'Playfair Display', Georgia, serif;
  --sans:'Open Sans', Arial, sans-serif;
}
*{box-sizing:border-box;margin:0;padding:0}
html,body{width:1200px;height:3208px;overflow:hidden}
body{position:relative;background:var(--white);font-family:var(--sans);color:var(--ink)}
.site-header{position:absolute;top:0;left:0;width:1200px;height:90px}
.brand{position:absolute;left:40px;top:22px;font-family:var(--serif);font-size:30px;font-weight:700;color:var(--ink);display:flex;align-items:center;gap:10px}
.brand .dot{width:14px;height:14px;border-radius:50%;background:var(--pink)}
.main-nav{position:absolute;right:40px;top:30px;display:flex;gap:6px}
.main-nav a{font-size:12px;font-weight:600;color:var(--ink);text-decoration:none;padding:6px 14px;letter-spacing:.5px}
.main-nav a.active{background:var(--pink);color:var(--white)}

.hero{position:absolute;top:90px;left:0;width:1200px;height:620px}
.hero-book{position:absolute;left:110px;top:40px;width:330px;height:480px;background:linear-gradient(160deg,#3c6a72,#b5382f 55%,#2b2f3d);box-shadow:12px 14px 22px rgba(0,0,0,.25)}
.hero-portrait{position:absolute;left:330px;top:20px;width:150px;height:150px;border-radius:50%;border:6px solid #222;background:linear-gradient(135deg,#c9a48a,#5a4a44)}
.hero-copy{position:absolute;left:600px;top:140px;width:420px;text-align:center}
.hero-title{font-family:var(--serif);font-size:50px;font-weight:900;letter-spacing:1px}
.hero-rule{height:1px;background:#ccc;margin:36px auto 0;width:300px}
.hero-tag{font-family:var(--serif);font-size:22px;margin-top:22px}
.hero-rule.bottom{margin-top:22px}
.btn-outline{display:inline-block;border:2px solid var(--pink);color:var(--pink);font-size:13px;font-weight:700;letter-spacing:2px;padding:13px 30px;margin-top:62px}

.band{position:absolute;left:0;width:1200px}
.torn{position:absolute;left:0;width:1200px;height:30px}
.mission-band{top:720px;height:720px;background:var(--pink)}
.section-label{font-size:14px;font-weight:700;letter-spacing:2px;text-align:center;color:var(--white)}
.mission-band .section-label{position:absolute;top:58px;width:100%}
.mission-quote{position:absolute;top:100px;left:290px;width:620px;text-align:center;color:var(--white);font-size:15px;line-height:1.7}
.quote-mark{position:absolute;top:90px;font-family:var(--serif);font-size:60px;color:var(--white);line-height:1}
.dots{position:absolute;top:228px;left:0;width:100%;text-align:center;color:var(--white);letter-spacing:6px;font-size:14px}
.band-divider{position:absolute;top:250px;left:0;width:100%;height:1px;background:rgba(255,255,255,.4)}
.features{position:absolute;top:310px;left:180px;width:840px;display:flex;justify-content:space-between}
.feature{width:220px;text-align:center;color:var(--white)}
.feature svg{width:44px;height:44px}
.feature h3{font-size:14px;letter-spacing:2px;margin-top:18px}
.feature p{font-size:11px;line-height:1.6;margin-top:12px;opacity:.9}
.btn-small{display:inline-block;border:1px solid currentColor;font-size:10px;font-weight:600;letter-spacing:1px;padding:6px 18px;margin-top:26px}

.books{top:1440px;height:610px;background:var(--grey)}
.books .section-label,.press .section-label{color:var(--pink);position:absolute;top:24px;width:100%}
.section-bar{position:absolute;top:52px;left:585px;width:30px;height:2px;background:var(--pink)}
.book-list{position:absolute;top:88px;left:160px;width:880px;display:flex;justify-content:space-between}
.book{width:220px;text-align:center}
.book-cover{height:320px;margin:0 auto;width:220px;box-shadow:4px 6px 12px rgba(0,0,0,.2)}
.book-title{font-size:13px;font-weight:600;margin-top:22px;letter-spacing:.5px}
.stars{color:var(--pink);font-size:13px;letter-spacing:2px;margin-top:6px}
.book .btn-small,.press-card .btn-small{color:var(--pink-soft);margin-top:18px}

.press{top:2050px;height:600px;background:var(--white)}
.press-list{position:absolute;top:170px;left:160px;width:888px;display:flex;justify-content:space-between}
.press-card{width:265px;height:410px;background:var(--grey);box-shadow:0 2px 6px rgba(0,0,0,.12)}
.press-photo{height:200px}
.press-card h4{font-size:15px;line-height:1.35;padding:20px 18px 0}
.press-card p{font-size:10.5px;line-height:1.55;color:var(--muted);padding:10px 18px 0}
.press-card .btn-small{margin-left:18px}

.footer{top:2650px;height:558px;background:var(--lilac)}
.footer-brand{position:absolute;top:190px;width:100%;text-align:center;font-family:var(--serif);font-size:40px;font-weight:700;color:var(--ink)}
.footer-nav{position:absolute;top:278px;width:100%;text-align:center;font-size:11px;letter-spacing:1.5px;color:var(--white)}
.footer-nav span{margin:0 10px}
.newsletter-label{position:absolute;top:318px;width:100%;text-align:center;font-size:11px;color:var(--white)}
.newsletter{position:absolute;top:350px;left:385px;width:430px;height:40px;background:var(--white);border-radius:20px;display:flex;align-items:center;justify-content:space-between;padding:0 20px;font-size:12px;color:var(--muted)}
.footer-rule{position:absolute;top:430px;left:160px;width:880px;height:1px;background:rgba(255,255,255,.5)}
.social{position:absolute;top:452px;left:160px;display:flex;align-items:center;gap:10px;font-size:11px;color:var(--white)}
.social i{display:block;width:22px;height:22px;border:1px solid var(--white);border-radius:3px}
.copyright{position:absolute;top:458px;right:160px;font-size:10px;color:var(--white)}
</style>
</head>
<body>

<header class="site-header">
  <div class="brand"><span class="dot"></span>Selina Marlowe</div>
  <nav class="main-nav">
    <a class="active">HOME</a><a>WORK</a><a>PRESS</a><a>CONTACT US</a>
  </nav>
</header>

<section class="hero">
  <div class="hero-book" role="img" aria-label="Book cover of Harbour at Heart, colourful street mural artwork"></div>
  <div class="hero-portrait" role="img" aria-label="Portrait photo of the author"></div>
  <div class="hero-copy">
    <h1 class="hero-title">HARBOUR AT HEART</h1>
    <div class="hero-rule"></div>
    <p class="hero-tag">Writer and Comics scholar</p>
    <div class="hero-rule bottom"></div>
    <a class="btn-outline">&#9993;&nbsp; SUBSCRIBE NOW</a>
  </div>
</section>

<section class="band mission-band">
  <svg class="torn" style="top:-14px" viewBox="0 0 1200 30" preserveAspectRatio="none"><polygon fill="#e0559e" points="0,14 40,8 90,16 150,6 220,14 300,9 380,16 460,7 540,13 620,8 700,16 780,6 860,13 940,9 1020,15 1100,7 1160,13 1200,9 1200,30 0,30"/></svg>
  <h2 class="section-label">MISSION</h2>
  <span class="quote-mark" style="left:250px">&ldquo;</span>
  <p class="mission-quote">Stories shape how we see our streets, our neighbours and ourselves. I write essays, fiction and comics criticism that look closely at the city and the people who draw it.</p>
  <span class="quote-mark" style="left:920px">&rdquo;</span>
  <div class="dots">&bull;&bull;&bull;</div>
  <div class="band-divider"></div>
  <div class="features">
    <div class="feature">
      <svg viewBox="0 0 44 44" fill="none" stroke="#fff" stroke-width="2"><rect x="6" y="8" width="28" height="20" rx="3"/><path d="M12 28v8l8-8"/><rect x="14" y="14" width="26" height="0" /></svg>
      <h3>BLOG</h3>
      <p>Notes on writing, reading and research, with fresh posts on comics, culture and city life each month.</p>
      <a class="btn-small">READ MORE</a>
    </div>
    <div class="feature">
      <svg viewBox="0 0 44 44" fill="none" stroke="#fff" stroke-width="2"><circle cx="22" cy="15" r="8"/><path d="M6 40c2-10 9-14 16-14s14 4 16 14"/></svg>
      <h3>ABOUT ME</h3>
      <p>Writer and scholar working across fiction, journalism and academic study of comics and graphic art.</p>
      <a class="btn-small">READ MORE</a>
    </div>
    <div class="feature">
      <svg viewBox="0 0 44 44" fill="none" stroke="#fff" stroke-width="2"><rect x="6" y="12" width="32" height="22" rx="2"/><path d="M6 13l16 12 16-12"/></svg>
      <h3>CONTACT US</h3>
      <p>88 Harbour Lane<br>Bayside, ON A1B 2C3<br>(555) 014-2290</p>
      <a class="btn-small">READ MORE</a>
    </div>
  </div>
</section>

<section class="band books">
  <svg class="torn" style="top:-16px" viewBox="0 0 1200 30" preserveAspectRatio="none"><polygon fill="#e0559e" points="0,0 1200,0 1200,14 1140,20 1060,12 980,19 900,11 820,18 740,12 660,20 580,13 500,19 420,11 340,18 260,12 180,20 100,13 40,18 0,12"/></svg>
  <h2 class="section-label">BOOKS</h2>
  <div class="section-bar"></div>
  <div class="book-list">
    <div class="book">
      <div class="book-cover" role="img" aria-label="Cover of Harbour at Heart, colourful mural artwork" style="background:linear-gradient(160deg,#3c6a72,#b5382f 55%,#2b2f3d)"></div>
      <div class="book-title">HARBOUR AT HEART</div>
      <div class="stars">&#9733;&#9733;&#9733;&#9733;&#9733;</div>
      <a class="btn-small">READ MORE</a>
    </div>
    <div class="book">
      <div class="book-cover" role="img" aria-label="Cover of Bayside Comics Volume 2, comic illustration" style="background:linear-gradient(180deg,#6e7fb6,#9a7fb8 50%,#3e4763)"></div>
      <div class="book-title">BAYSIDE COMICS VOLUME 2</div>
      <div class="stars">&#9733;&#9733;&#9733;&#9733;&#9733;</div>
      <a class="btn-small">READ MORE</a>
    </div>
    <div class="book">
      <div class="book-cover" role="img" aria-label="Cover of a fiction anthology, orange and black design" style="background:linear-gradient(180deg,#2b2b2b 0 35%,#f08a2c 35% 100%)"></div>
      <div class="book-title">FICTION</div>
      <div class="stars">&#9733;&#9733;&#9733;&#9733;&#9733;</div>
      <a class="btn-small">READ MORE</a>
    </div>
  </div>
</section>

<section class="band press">
  <h2 class="section-label">PRESS</h2>
  <div class="section-bar"></div>
  <div class="press-list">
    <article class="press-card">
      <div class="press-photo" role="img" aria-label="Photo of comic anthology pages" style="background:linear-gradient(135deg,#8fa6c9,#d6b9c9)"></div>
      <h4>The Bayside Comics anthology series showcases rising talent</h4>
      <p>A look at how the anthology gives new local creators a place to publish stories about their city.</p>
      <a class="btn-small">READ MORE</a>
    </article>
    <article class="press-card">
      <div class="press-photo" role="img" aria-label="Portrait photo of the author outdoors" style="background:linear-gradient(135deg,#7e9b7a,#4a4338)"></div>
      <h4>Campus Profile: Selina Marlowe</h4>
      <p>The doctoral researcher talks about comics, communication and writing for readers of all kinds.</p>
      <a class="btn-small">READ MORE</a>
    </article>
    <article class="press-card">
      <div class="press-photo" role="img" aria-label="Photo of the author holding a book" style="background:linear-gradient(135deg,#cfcac6,#5b5552)"></div>
      <h4>Open Page Interviews: Selina Marlowe, Writer &ldquo;Harbour at Heart&rdquo;</h4>
      <p>The writer discusses her new story in the latest anthology and the streets that inspired it.</p>
      <a class="btn-small">READ MORE</a>
    </article>
  </div>
</section>

<footer class="band footer">
  <svg class="torn" style="top:-16px" viewBox="0 0 1200 30" preserveAspectRatio="none"><polygon fill="#b7a5cd" points="0,14 60,8 130,16 210,7 290,14 370,9 450,17 530,8 610,14 690,7 770,15 850,9 930,16 1010,8 1090,14 1160,8 1200,13 1200,30 0,30"/></svg>
  <div class="footer-brand">Selina Marlowe</div>
  <div class="footer-nav"><span>HOME</span><span>WORK</span><span>PRESS</span><span>CONTACT</span></div>
  <div class="newsletter-label">Newsletter sign up</div>
  <div class="newsletter"><span>E-mail Address</span><span style="color:var(--ink)">&rarr;</span></div>
  <div class="footer-rule"></div>
  <div class="social">Follow us <i></i><i></i><i></i><i></i></div>
  <div class="copyright">Copyright &copy; Selina Marlowe. All rights reserved.</div>
</footer>

</body>
</html>
```